Business Card Design Project

Hi
I'm currently getting a logo designed which will go on the front. It is designed for s
Fitness instructor/ personal training business.
On the back I would like written:
Boxing for Fitness
Aqua Fitness Professional
PersonalisedTraining 1/1 or Small Group outdoor training
Fun and unique workouts
Weight loss/ Strength training

Also I need on there my details
minaharker27@quellmail.net
0438 917 355
FB Mina Fitness

Reason: I would like to extend the deadline to give extra days after I have confirmed the logo in two days

Target Market(s)

Mostly women aged between 20-50

Industry/Entity Type

Training

Font styles to use
Sans Serif

Requirements
Must have
• My logo ( I have attached my favourite logo options )
My details

```html
<!DOCTYPE html>
<html lang="en">
<head>
<meta charset="utf-8">
<title>Mina Fitness – Business Card</title>
<link href="https://fonts.googleapis.com/css2?family=Arimo:wght@400;700&display=swap" rel="stylesheet">
<style>
  :root {
    --backdrop: #e9e9e9;
    --front-green: #86df00;
    --back-blue: #0077f5;
    --ink-light: #ffffff;
  }
  * { margin: 0; padding: 0; box-sizing: border-box; }
  html, body {
    width: 1196px;
    height: 1200px;
    overflow: hidden;
  }
  body {
    background: var(--backdrop);
    font-family: "Arimo", Arial, sans-serif;
    color: var(--ink-light);
    position: relative;
  }
  .card {
    position: absolute;
    left: 256px;
    width: 684px;
    height: 343px;
  }
  .card-front {
    top: 234px;
    background: var(--front-green);
    display: flex;
    align-items: center;
    justify-content: center;
  }
  .card-back {
    top: 616px;
    background: var(--back-blue);
  }

  .brand-mark {
    display: flex;
    align-items: center;
    gap: 14px;
  }
  .brand-ring {
    width: 74px;
    height: 74px;
    border: 3px solid var(--ink-light);
    border-radius: 50%;
    flex: none;
  }
  .brand-name {
    font-weight: 700;
    font-size: 46px;
    letter-spacing: 0.5px;
    white-space: nowrap;
  }
  .brand-mark.small { gap: 6px; }
  .brand-mark.small .brand-ring { width: 24px; height: 24px; border-width: 1.5px; }
  .brand-mark.small .brand-name { font-size: 15px; }

  .services {
    position: absolute;
    left: 67px;
    top: 66px;
  }
  .services-title {
    font-size: 20px;
    font-weight: 400;
    margin-bottom: 19px;
  }
  .services-list { list-style: none; }
  .services-list li {
    position: relative;
    padding-left: 17px;
    font-size: 16px;
    line-height: 1.2;
    margin-bottom: 13px;
  }
  .services-list li::before {
    content: "";
    position: absolute;
    left: 2px;
    top: 8px;
    width: 4px;
    height: 4px;
    background: var(--ink-light);
  }
  .services-list .note {
    display: block;
    font-size: 11px;
    margin-top: 2px;
  }

  .divider {
    position: absolute;
    left: 342px;
    top: 35px;
    width: 2px;
    height: 273px;
    background: var(--ink-light);
  }

  .contact {
    position: absolute;
    left: 411px;
    top: 68px;
  }
  .contact-label { font-size: 12px; line-height: 1.2; }
  .contact-value { font-size: 17px; line-height: 1.3; margin-bottom: 17px; }
  .contact-social { font-size: 16px; font-weight: 700; line-height: 1.2; margin-top: 6px; }
  .contact-role { font-size: 12px; line-height: 1.2; }

  .card-back .brand-mark.small {
    position: absolute;
    left: 528px;
    top: 240px;
  }
</style>
</head>
<body>
  <section class="card card-front">
    <div class="brand-mark">
      <span class="brand-ring"></span>
      <span class="brand-name">Mina Fitness</span>
    </div>
  </section>

  <section class="card card-back">
    <div class="services">
      <h2 class="services-title">Training Lessons</h2>
      <ul class="services-list">
        <li>Weight loss/Strength training</li>
        <li>Aqua Fitness Professional</li>
        <li>Personalised Training 1/1<span class="note">or Small Group outdoor training</span></li>
        <li>Boxing for Fitness</li>
        <li>Fun and unique workouts</li>
      </ul>
    </div>

    <div class="divider"></div>

    <div class="contact">
      <p class="contact-label">mail</p>
      <p class="contact-value">minaharker27@quellmail.net</p>
      <p class="contact-label">tel</p>
      <p class="contact-value">0438 917 355</p>
      <p class="contact-social">FB Mina Fitness</p>
      <p class="contact-role">Personal Training</p>
    </div>

    <div class="brand-mark small">
      <span class="brand-ring"></span>
      <span class="brand-name">Mina Fitness</span>
    </div>
  </section>
</body>
</html>
```